Wordpress Design Project (Dellowin)

We need a wordpress design for an established auction and real estate company based in New Jersey. The winning design will incorporate a professional color scheme and company logo in a clean layout.

Industry/Entity Type

Real Estate

Requirements
Must have
• - We will require winning designer to provide a layered PSD (Adobe photoshop) concept file, along with any non-standard font files used.

Logo attached. Will hopefully post better logo shortly. Please use site design colors of your choice as the logo is black & white. A site client mentions liking is http://www.qrtbidhouse.example/. Homepage content will be an auction list as seen at http://www.gavelroster.example/?page=5

Horizontal Navigation menu with these pages:
Home - Auction Calendar - Appraisals - Services - Company Profile - News & Events - Testimonials - Contact Us

A slideshow element on the home page using one of the placeholder images provided (or stock if higher resolution image is necessary).

Sidebar widgets to be included are: Email sign-up form - Featured Auctions - Testimonial widget - 'Our Videos' widget; Social media icons somewhere in layout (facebook, twitter, RSS, and Youtube)

Homepage content is text:
DELLOWIN OVERSIGHT COMPANY was founded 90 years ago in 1921 by Harold Dellowin, which makes us one of the oldest commercial and industrial auction and appraisal companies in America.

We have conducted thousands of auctions, assisting a wide range of companies both large and small achieve maximum value for their capital assets.
Nice to have
• - Site will have drop down menus, nice to have a sample look for them on one of the primary menu items.

```html
<!DOCTYPE html>
<html lang="en">
<head>
<meta charset="utf-8">
<title>Dellowin Oversight Company</title>
<link href="https://fonts.googleapis.com/css2?family=Arvo:ital,wght@0,400;0,700;1,400&family=Open+Sans:wght@400;600&display=swap" rel="stylesheet">
<style>
:root{
  --ink:#1c1c1c;
  --text:#3a3a3a;
  --muted:#555;
  --red:#d0173a;
  --red-dark:#a80f2c;
  --nav:#1f1f1f;
  --nav-line:#3a3a3a;
  --panel:#e6e6e6;
  --panel-edge:#cfcfcf;
  --footer:#262626;
  --white:#fff;
}
*{box-sizing:border-box;margin:0;padding:0}
html,body{width:963px;height:1200px;overflow:hidden}
body{position:relative;background:radial-gradient(ellipse at 50% 0%,#fafafa 0%,#e4e4e4 70%,#dcdcdc 100%);font-family:"Arvo",serif;color:var(--text)}
.abs{position:absolute}

.brand{left:72px;top:19px;display:flex;align-items:center;gap:8px}
.brand-square{width:34px;height:34px;background:var(--ink)}
.brand-name{font-family:"Arvo",serif;font-weight:700;font-size:30px;color:var(--ink);letter-spacing:1px}

.phone{right:77px;top:44px;display:flex;align-items:center;gap:8px;font-family:"Open Sans",sans-serif;font-weight:600;font-size:19px;color:var(--ink);letter-spacing:.5px}
.phone-badge{width:20px;height:20px;background:var(--red);border-radius:3px;display:flex;align-items:center;justify-content:center}

.nav{left:69px;top:80px;width:826px;height:43px;background:var(--nav);padding:4px}
.nav-inner{height:100%;border:1px solid var(--nav-line);display:flex;justify-content:space-around;align-items:center;font-family:"Open Sans",sans-serif;font-size:12.5px;color:#e8e8e8}
.dropdown{left:373px;top:123px;width:158px;background:#202020;border:1px solid #3a3a3a;border-top:none;padding:3px;font-family:"Open Sans",sans-serif;font-size:12.5px;color:#e0e0e0;z-index:3}
.dropdown li{list-style:none;height:27px;line-height:27px;padding-left:9px;border-bottom:1px solid #3a3a3a}
.dropdown li:last-child{border-bottom:none}

.slider{left:69px;top:131px;width:568px;height:288px;background:#262626;padding:8px 6px 9px 10px;box-shadow:0 12px 14px -8px rgba(0,0,0,.35)}
.slide-fill{width:100%;height:100%;background:linear-gradient(180deg,#5f9ad6 0%,#a9c9ea 35%,#c02a33 55%,#9e1d25 75%,#6f6e6c 100%)}

.overview{left:644px;top:131px;width:250px;height:288px;background:#e2e2e2;border:1px solid var(--panel-edge);padding:4px}
.overview-inner{height:100%;border:1px dotted #bdbdbd;padding:10px 8px}
.overview h2{font-weight:400;font-size:17px;color:#555;text-align:center;padding-bottom:8px;border-bottom:1px solid #c9c9c9;white-space:nowrap}
.overview p{font-size:10.6px;line-height:16px;text-align:justify;margin-top:11px;color:#2e2e2e}
.overview strong{font-weight:400;color:var(--ink)}
.btn-dark{right:12px;top:250px;width:94px;height:26px;background:#1e1e1e;color:#fff;font-family:"Open Sans",sans-serif;font-size:12px;display:flex;align-items:center;justify-content:center}

.featured{left:66px;top:450px;width:557px;height:608px;background:var(--panel)}
.featured h2{position:absolute;left:19px;top:14px;font-weight:400;font-size:20px;color:#333;letter-spacing:.5px}
.auction{position:absolute;left:13px;width:530px;height:187px}
.thumb{position:absolute;left:0;top:0;width:106px;height:80px;border:3px solid #fff;box-shadow:0 0 2px rgba(0,0,0,.3);background:linear-gradient(180deg,#7fb0dc 0%,#b7cfe5 40%,#e9e9e9 60%,#8b8a85 100%)}
.btn{position:absolute;left:0;width:106px;height:24px;border-radius:12px;color:#fff;font-family:Arial,sans-serif;font-size:11px;display:flex;align-items:center;padding-left:10px;gap:12px}
.btn-details{top:86px;background:linear-gradient(#ee3a59,#c8102f);border:1px solid #fff;box-shadow:0 0 0 1px #c8102f}
.btn-gallery{top:114px;background:linear-gradient(#4a4040,#1c1414);border:1px solid #fff;box-shadow:0 0 0 1px #222}
.auction h3{position:absolute;left:118px;top:1px;font-weight:400;font-style:italic;font-size:14.3px;color:var(--red)}
.auction .desc{position:absolute;left:118px;top:26px;width:408px;font-family:"Open Sans",sans-serif;font-size:11.6px;line-height:15.2px;color:#4a4a4a;text-align:justify}
.auction .meta{position:absolute;left:118px;top:97px;font-size:11.8px;line-height:15.2px;color:#222}
.auction .rule{position:absolute;left:0;top:164px;width:527px;border-top:1px dotted #aaa}

.email{left:644px;top:449px;width:250px;height:197px;background:linear-gradient(180deg,#c51a3c,#a60f2c);border:1px solid #8c0a22;color:#fff;text-align:center}
.email h2{position:absolute;left:0;right:0;top:16px;font-weight:400;font-size:19.5px;letter-spacing:.4px}
.email .field{position:absolute;left:20px;top:52px;width:213px;height:24px;border:1px solid #7c0a20;background:rgba(0,0,0,.12);font-size:11.5px;text-align:left;padding-left:8px;line-height:22px}
.email .subscribe{position:absolute;left:70px;top:88px;width:101px;height:21px;background:linear-gradient(#444,#151515);border-radius:4px;font-family:"Open Sans",sans-serif;font-size:11px;line-height:21px}
.email .big{position:absolute;left:0;right:0;top:125px;font-size:31px;color:#f5c9d1}
.email .call{position:absolute;left:0;right:0;top:168px;font-size:17px}

.video{left:647px;top:667px;width:245px;height:188px;background:#1b1b1b;padding:6px 6px 0}
.video-fill{width:100%;height:157px;background:linear-gradient(135deg,#6b5a45 0%,#bdb4a0 40%,#d7d2c6 60%,#7f7464 100%)}
.video-bar{height:25px;display:flex;align-items:center;gap:6px;padding:0 2px}
.video-track{flex:1;height:2px;background:#555}

.says{left:645px;top:880px;width:249px;text-align:center;font-weight:400;font-size:19px;color:#444}
.bubble{left:645px;top:909px;width:249px;height:140px;background:#ececec;border:2px solid #fff;border-radius:14px;box-shadow:0 1px 3px rgba(0,0,0,.15);padding:16px 11px 0 8px;font-style:italic;font-size:12.3px;line-height:17px;text-align:justify;color:#333}
.bubble-tail{left:838px;top:1046px}
.posted{left:666px;top:1055px;font-style:italic;font-size:13px;color:#555}
.posted span{font-style:normal;color:var(--red);font-size:15px}

.footer{left:0;top:1109px;width:963px;height:91px;background:var(--footer)}
.footer .brand{left:73px;top:26px}
.footer .brand-square{background:#fff}
.footer .brand-name{color:#fff}
.copy{left:412px;top:51px;font-family:Arial,sans-serif;font-size:11px;color:#fff}
.connected{left:744px;top:15px;font-size:14.5px;color:#ddd}
.socials{left:739px;top:39px;display:flex;gap:12px}
.socials span{width:28px;height:28px;border-radius:50%;border:2px solid #ddd}
</style>
</head>
<body>

<div class="abs brand"><span class="brand-square"></span><span class="brand-name">DELLOWIN</span></div>

<div class="abs phone">
  <span class="phone-badge"><svg width="12" height="12" viewBox="0 0 24 24"><path fill="#fff" d="M6.6 10.8a15.1 15.1 0 006.6 6.6l2.2-2.2c.3-.3.7-.4 1-.2 1.1.4 2.3.6 3.6.6.6 0 1 .4 1 1V20c0 .6-.4 1-1 1A17 17 0 013 4c0-.6.4-1 1-1h3.5c.6 0 1 .4 1 1 0 1.3.2 2.5.6 3.6.1.3 0 .7-.2 1z"/></svg></span>
  555-210-4477
</div>

<nav class="abs nav"><div class="nav-inner">
  <span>Home</span><span>Auction Calendar</span><span>Appraisals</span><span>Services</span><span>Company Profile</span><span>News &amp; Events</span><span>Testimonials</span><span>Contact Us</span>
</div></nav>

<ul class="abs dropdown">
  <li>Category One</li><li>Category Two</li><li>Category Three</li>
</ul>

<div class="abs slider"><div class="slide-fill" role="img" aria-label="Row of red semi-trucks parked under a blue sky"></div></div>

<section class="abs overview"><div class="overview-inner">
  <h2>COMPANY OVERVIEW</h2>
  <p><strong>DELLOWIN OVERSIGHT COMPANY</strong> was founded 90 years ago in 1921 by Harold Dellowin, which makes us one of the oldest commercial and industrial auction and appraisal companies in America.</p>
  <p>We have conducted thousands of auctions, assisting a wide range of companies both large and small achieve maximum value for their capital assets.</p>
  <span class="abs btn-dark">Read More</span>
</div></section>

<section class="abs featured">
  <h2>FEATURED AUCTIONS</h2>

  <article class="auction" style="top:56px">
    <div class="thumb" role="img" aria-label="White flatbed pickup truck"></div>
    <span class="btn btn-details"><svg width="11" height="11"><rect x="0" y="0" width="3" height="3" fill="#fff"/><rect x="0" y="4" width="3" height="3" fill="#fff"/><rect x="0" y="8" width="3" height="3" fill="#fff"/><rect x="5" y="0" width="6" height="3" fill="#fff"/><rect x="5" y="4" width="6" height="3" fill="#fff"/><rect x="5" y="8" width="6" height="3" fill="#fff"/></svg>Details Now</span>
    <span class="btn btn-gallery"><svg width="14" height="11"><rect x="0.5" y="0.5" width="13" height="10" fill="none" stroke="#fff"/><path d="M2 9l4-4 3 3 2-2 2 3z" fill="#fff"/></svg>Gallery</span>
    <h3>2005 Hadley Ranger 3500 Torvex Turbo Diesel Flatbed</h3>
    <p class="desc">2005 Hadley Ranger 3500 Torvex Turbo Diesel Flatbed 4x4 Truck Online auction at www.bidwestward.example - Tuesday, August 13, 2013 at 10:00 am. Due to bankruptcy, this Hadley Ranger 3500 must be sold! Features include automatic transmission, leather seats, fo...</p>
    <p class="meta">Live On-Site Auction<br>Begins: &nbsp;Tuesday, August 13, 2013 at 10:00 AM EDT<br>Location: 218 Marlow Crest Road, Fairbrook, CA 90000</p>
    <div class="rule"></div>
  </article>

  <article class="auction" style="top:243px">
    <div class="thumb" role="img" aria-label="White flatbed pickup truck"></div>
    <span class="btn btn-details"><svg width="11" height="11"><rect x="0" y="0" width="3" height="3" fill="#fff"/><rect x="0" y="4" width="3" height="3" fill="#fff"/><rect x="0" y="8" width="3" height="3" fill="#fff"/><rect x="5" y="0" width="6" height="3" fill="#fff"/><rect x="5" y="4" width="6" height="3" fill="#fff"/><rect x="5" y="8" width="6" height="3" fill="#fff"/></svg>Details Now</span>
    <span class="btn btn-gallery"><svg width="14" height="11"><rect x="0.5" y="0.5" width="13" height="10" fill="none" stroke="#fff"/><path d="M2 9l4-4 3 3 2-2 2 3z" fill="#fff"/></svg>Gallery</span>
    <h3>2005 Hadley Ranger 3500 Torvex Turbo Diesel Flatbed</h3>
    <p class="desc">2005 Hadley Ranger 3500 Torvex Turbo Diesel Flatbed 4x4 Truck Online auction at www.bidwestward.example - Tuesday, August 13, 2013 at 10:00 am. Due to bankruptcy, this Hadley Ranger 3500 must be sold! Features include automatic transmission, leather seats, fo...</p>
    <p class="meta">Live On-Site Auction<br>Begins: &nbsp;Tuesday, August 13, 2013 at 10:00 AM EDT<br>Location: 218 Marlow Crest Road, Fairbrook, CA 90000</p>
    <div class="rule"></div>
  </article>

  <article class="auction" style="top:430px">
    <div class="thumb" role="img" aria-label="White flatbed pickup truck"></div>
    <span class="btn btn-details"><svg width="11" height="11"><rect x="0" y="0" width="3" height="3" fill="#fff"/><rect x="0" y="4" width="3" height="3" fill="#fff"/><rect x="0" y="8" width="3" height="3" fill="#fff"/><rect x="5" y="0" width="6" height="3" fill="#fff"/><rect x="5" y="4" width="6" height="3" fill="#fff"/><rect x="5" y="8" width="6" height="3" fill="#fff"/></svg>Details Now</span>
    <span class="btn btn-gallery"><svg width="14" height="11"><rect x="0.5" y="0.5" width="13" height="10" fill="none" stroke="#fff"/><path d="M2 9l4-4 3 3 2-2 2 3z" fill="#fff"/></svg>Gallery</span>
    <h3>2005 Hadley Ranger 3500 Torvex Turbo Diesel Flatbed</h3>
    <p class="desc">2005 Hadley Ranger 3500 Torvex Turbo Diesel Flatbed 4x4 Truck Online auction at www.bidwestward.example - Tuesday, August 13, 2013 at 10:00 am. Due to bankruptcy, this Hadley Ranger 3500 must be sold! Features include automatic transmission, leather seats, fo...</p>
    <p class="meta">Live On-Site Auction<br>Begins: &nbsp;Tuesday, August 13, 2013 at 10:00 AM EDT<br>Location: 218 Marlow Crest Road, Fairbrook, CA 90000</p>
  </article>
</section>

<section class="abs email">
  <h2>JOIN OUR EMAIL LIST:</h2>
  <div class="field">Your Email</div>
  <div class="subscribe">Subscribe Now</div>
  <div class="big">For Details</div>
  <div class="call">Call us on: (555) 318 6620</div>
</section>

<section class="abs video">
  <div class="video-fill" role="img" aria-label="Video still of an industrial printing press"></div>
  <div class="video-bar">
    <svg width="10" height="10" viewBox="0 0 10 10"><circle cx="5" cy="5" r="5" fill="#ddd"/><path d="M4 3l3 2-3 2z" fill="#1b1b1b"/></svg>
    <span class="video-track"></span>
    <svg width="40" height="8"><rect x="0" y="1" width="10" height="6" fill="#888"/><rect x="14" y="1" width="4" height="6" fill="#ccc"/><rect x="22" y="3" width="18" height="2" fill="#ccc"/></svg>
  </div>
</section>

<h2 class="abs says">WHAT CLIENT SAYS !!</h2>
<blockquote class="abs bubble">&ldquo;Suspendisse vulputate aliquam dui. Nulla elementum dui ut augue. Aliquam vehicula mi at mauris. Maecenas placerat, nisl at consequat rhoncus, sem nunc gravida justo, quis eleifend arcu velit quis lacus.&rdquo;</blockquote>
<svg class="abs bubble-tail" width="40" height="30" viewBox="0 0 40 30"><path d="M2 0 L38 0 L6 28 Z" fill="#ececec" stroke="#fff" stroke-width="2"/><rect x="0" y="0" width="40" height="3" fill="#ececec"/></svg>
<p class="abs posted">Posted By: <span>Alan Pryce</span></p>

<footer class="abs footer">
  <div class="abs brand"><span class="brand-square"></span><span class="brand-name">DELLOWIN</span></div>
  <p class="abs copy">Copyright &copy; Dellowin &amp; Auctioneers.</p>
  <p class="abs connected">GET CONNECTED</p>
  <div class="abs socials" aria-label="Social links"><span></span><span></span><span></span><span></span></div>
</footer>

</body>
</html>
```